My company Ember Atelier, founded in 2004 and based in downtown Brooklyn, NY, is a design firm specializing in furniture and residential projects, primarily apartments in New York City but also houses in the New York area. The built projects are distinctly modern, and the furniture (large wooden constructions that hold books and objects) border on sculpture. I also do a fair amount of photography and drawing, so my ideal client is someone who collects current art and photography and wants a space commensurate with that interest. The purpose of the website is twofold. First, to attract a clientele for residential projects who have a strong interest in contemporary art, and secondly, to develop a platform for selling my furniture on a made-to-order basis. The website, and especially the landing page, should visualize my preference for raw materials-construction lumber, plywood, concrete, exposed bolts and screws, etc. I like bold colors, graffiti, accidental marks, and all species of imperfection. Slick and ultra-stylized is not my thing. With regard to typeface, I like it simple and unadorned, but assertive, and handwritten is an option as long as it is bold. The landing page could simply be a background featuring one of the above preferences, with EMBER ATELIER overlaid in black (or colored?) type and a small 'enter' button to an index page, but I'm open to suggestions. See additional directions below...Thanks!

Target Market(s)

People interested in contemporary art, photography, architecture and design

Industry/Entity Type

Residential

Requirements
Must have
• All I would like to see initially is a landing page and index page. The landing page as stated above should have a material background-see attached photos (any will do) with the company name and enter button.
The index page should include the following categories with links to be designed later: About, Portfolio, Purchase Furniture, Contact. Use a second material background from the attached photos for the index page. NOTE: please use the concrete slab photo on one of the pages, the other page can have either plywood or carboard, whichever works best for your design. If you want to replicate the ply or cardboard in a grid that's fine too
Should not have
• Since I take an ipad when I meet with clients the site cannot utilize Flash. Also no sound.

```html
<!DOCTYPE html>
<html lang="en">
<head>
<meta charset="utf-8">
<title>Ember Atelier — Index</title>
<link rel="stylesheet" href="https://fonts.googleapis.com/css2?family=Russo+One&display=swap">
<style>
  :root {
    --wood-light: #b8671f;
    --wood-mid: #8f4a14;
    --wood-dark: #3a1a06;
    --veil: rgba(255, 236, 214, 0.32);
    --veil-strong: rgba(250, 232, 214, 0.86);
    --ink: #000000;
    --burnt: #8b4814;
    --contact-block: #2b1409;
    --contact-ink: #ecd2b8;
    --edge: rgba(30, 12, 2, 0.85);
  }
  * { margin: 0; padding: 0; box-sizing: border-box; }
  html, body { width: 1200px; height: 900px; overflow: hidden; }
  body { font-family: "Russo One", sans-serif; }

  .index-page { position: relative; width: 1200px; height: 900px; overflow: hidden; }

  .wood-surface {
    position: absolute; inset: 0;
    background:
      radial-gradient(ellipse 75% 70% at 50% 48%, rgba(0,0,0,0) 45%, rgba(30,10,0,0.7) 100%),
      linear-gradient(178deg, var(--wood-mid) 0%, var(--wood-light) 40%, #a9591a 65%, var(--wood-mid) 100%);
  }

  .brand { position: absolute; left: 72px; top: 212px; color: var(--ink); font-size: 62px; line-height: 0.82; letter-spacing: -1px; text-transform: lowercase; }
  .brand span { display: block; }
  .brand .brand-second { margin-left: 38px; }

  .band { position: absolute; background: var(--veil); }
  .band-about { left: 220px; top: 348px; width: 755px; height: 88px; }
  .band-rail { left: 0; top: 472px; width: 720px; height: 12px; }
  .band-stem-about { left: 540px; top: 436px; width: 8px; height: 36px; }
  .band-stem-portfolio { left: 478px; top: 484px; width: 13px; height: 46px; }
  .band-purchase { left: 719px; top: 471px; width: 373px; height: 60px; }

  .edge { position: absolute; background: var(--edge); }
  .edge-about-right { left: 973px; top: 348px; width: 3px; height: 296px; }
  .edge-about-base { left: 545px; top: 435px; width: 430px; height: 2px; }
  .edge-portfolio { left: 295px; top: 530px; width: 3px; height: 370px; }

  .block-portfolio { position: absolute; left: 298px; top: 530px; width: 262px; height: 370px; background: var(--veil-strong); }
  .block-contact { position: absolute; left: 749px; top: 644px; width: 451px; height: 256px;
    background: linear-gradient(135deg, #3a1c0b 0%, var(--contact-block) 60%, #1c0c04 100%); }

  .nav-link { position: absolute; text-decoration: none; font-size: 46px; line-height: 1; text-transform: lowercase; }
  .nav-about { left: 521px; top: 370px; color: var(--burnt); }
  .nav-purchase { left: 776px; top: 478px; color: var(--burnt); }
  .nav-portfolio { left: 318px; top: 626px; color: var(--burnt); }
  .nav-contact { left: 880px; top: 736px; color: var(--contact-ink); }
</style>
</head>
<body>
<main class="index-page">
  <div class="wood-surface" role="img" aria-label="Warm oak wood grain surface with darkened vignette edges"></div>

  <h1 class="brand"><span class="brand-first">ember</span><span class="brand-second">atelier</span></h1>

  <div class="band band-about"></div>
  <div class="band band-stem-about"></div>
  <div class="band band-rail"></div>
  <div class="band band-stem-portfolio"></div>
  <div class="band band-purchase"></div>

  <div class="block-portfolio"></div>
  <div class="block-contact"></div>

  <div class="edge edge-about-right"></div>
  <div class="edge edge-about-base"></div>
  <div class="edge edge-portfolio"></div>

  <nav>
    <a class="nav-link nav-about" href="#about">about</a>
    <a class="nav-link nav-purchase" href="#purchase">purchase</a>
    <a class="nav-link nav-portfolio" href="#portfolio">portfolio</a>
    <a class="nav-link nav-contact" href="#contact">contact</a>
  </nav>
</main>
</body>
</html>
```